Private Security Company Business Card and Logo Design

Looking for a modern conservative business card design for our new private security company Halvern Guard Partners, Inc. or HGP for short.
Private Security Services. The current logo we have is not very good and honestly would like a sharp logo for the card instead of using the one we have now. Open to ideas. I am easy just looking for something nicer then what I can personally design on cardloomix. I searched on zintrova for Security Company business cards went to images and found some nice designs that were made here.

Target Market(s)

Security Services

Industry/Entity Type

Business

Contact Information for Business Card

Halvern Guard Partners, Inc.
President, cell,office,fax,email, website,
Logo etc, whatever is needed for a standard business card
Can provide personal Information later.

Colors
0556a4
ffffff
474747

Requirements
Must have
• Modern but conservative,
Nice to have
• color choices
• Blue, white, Grey

```html
<!DOCTYPE html>
<html lang="en">
<head>
<meta charset="utf-8">
<title>Halvern Guard Partners, Inc. — Business Card</title>
<link rel="stylesheet" href="https://fonts.googleapis.com/css2?family=Questrial&display=swap">
<style>
  :root {
    --page-bg: #d9d9dc;
    --card-dark: #0b0b0d;
    --card-mid: #1c1c20;
    --brand-blue: #0556a4;
    --name-blue: #2f6fd6;
    --text-white: #ffffff;
    --text-grey: #c9c9cc;
    --mark-grey: #474747;
    --watermark: rgba(255,255,255,0.05);
  }
  * { box-sizing: border-box; margin: 0; padding: 0; }
  html, body {
    width: 1200px; height: 784px; overflow: hidden;
    background: var(--page-bg);
    font-family: "Questrial", "Century Gothic", sans-serif;
  }
  .sheet {
    width: 1200px; height: 784px;
    display: flex; align-items: center; justify-content: center; gap: 40px;
  }
  .card {
    position: relative;
    width: 540px; height: 309px;
    background: radial-gradient(ellipse at 60% 40%, var(--card-mid) 0%, var(--card-dark) 75%);
    overflow: hidden;
    box-shadow: 0 10px 28px rgba(0,0,0,0.25);
  }

  /* contact side */
  .card-back .watermark {
    position: absolute; left: 18px; top: 40px;
    font-size: 150px; letter-spacing: 4px;
    color: var(--watermark);
    line-height: 1;
  }
  .contact {
    position: absolute; left: 250px; top: 34px;
    color: var(--text-white);
  }
  .contact-name { font-size: 22px; color: var(--name-blue); }
  .contact-title { font-size: 11px; margin-top: 4px; margin-bottom: 14px; color: var(--text-white); }
  .contact-list { list-style: none; }
  .contact-list li {
    display: flex; align-items: center; gap: 7px;
    font-size: 13px; line-height: 17px; color: var(--text-white);
  }
  .contact-list svg { width: 11px; height: 11px; flex: none; }

  /* logo side */
  .card-front { display: flex; flex-direction: column; align-items: center; justify-content: center; }
  .brand-mark {
    display: flex; align-items: center; gap: 10px;
    font-size: 46px; color: var(--text-grey); letter-spacing: 3px;
  }
  .brand-mark .mark-square { width: 18px; height: 18px; background: var(--brand-blue); }
  .brand-name {
    margin-top: 22px;
    font-size: 22px; color: var(--text-grey); letter-spacing: 1px;
  }
</style>
</head>
<body>
<main class="sheet">
  <section class="card card-back" aria-label="Contact side">
    <div class="watermark" aria-hidden="true">HGP</div>
    <div class="contact">
      <p class="contact-name">Darren Whitlock</p>
      <p class="contact-title">President</p>
      <ul class="contact-list">
        <li>
          <svg viewBox="0 0 12 12" aria-hidden="true"><rect x="3" y="0.5" width="6" height="11" rx="1" fill="none" stroke="#2f6fd6" stroke-width="1.2"/><circle cx="6" cy="9.5" r="0.8" fill="#2f6fd6"/></svg>
          190 5521 604
        </li>
        <li>
          <svg viewBox="0 0 12 12" aria-hidden="true"><path d="M2 1 L4.5 1 L5.5 3.5 L4 4.8 Q5.5 7.5 7.2 8 L8.5 6.5 L11 7.5 L11 10 Q6 11.5 1 2 Z" fill="#2f6fd6"/></svg>
          104 7730 258
        </li>
        <li>
          <svg viewBox="0 0 12 12" aria-hidden="true"><rect x="0.7" y="2.5" width="10.6" height="7" fill="none" stroke="#2f6fd6" stroke-width="1.2"/><path d="M1 3 L6 7 L11 3" fill="none" stroke="#2f6fd6" stroke-width="1.2"/></svg>
          dwhitlock@halvernguard.com
        </li>
        <li>
          <svg viewBox="0 0 12 12" aria-hidden="true"><circle cx="6" cy="6" r="5" fill="none" stroke="#2f6fd6" stroke-width="1.2"/><path d="M1 6 H11 M6 1 Q3 6 6 11 M6 1 Q9 6 6 11" fill="none" stroke="#2f6fd6" stroke-width="1"/></svg>
          www.halvernguard.com
        </li>
        <li>
          <svg viewBox="0 0 12 12" aria-hidden="true"><path d="M6 11 Q1.5 6 2 4.5 A4 4 0 0 1 10 4.5 Q10.5 6 6 11 Z" fill="#2f6fd6"/><circle cx="6" cy="4.5" r="1.4" fill="#0b0b0d"/></svg>
          18 Marlow Lane, R D 4, Ashby 0417
        </li>
      </ul>
    </div>
  </section>

  <section class="card card-front" aria-label="Logo side">
    <div class="brand-mark"><span class="mark-square" aria-hidden="true"></span>HGP</div>
    <p class="brand-name">Halvern Guard Partners, Inc.</p>
  </section>
</main>
</body>
</html>
```